Bertrand Music Video and Film Production

THE FLYER SHOULD INCLUDE THIS TEXT:

"PROFESSIONAL FILM AND MUSIC VIDEO DIRECTzOR WITH OVER 10 YEARS EXPERIENCE. CLIENT LIST INCLUDES, 518, MARDEWICK, QUEEN LANTERNS, BRACKENMOOR, THE PLOVERS, TAN FOG, DORA-MAE, JUNE FARROW, OVX, PINECONE.
HD, SUPER 8, LIVE DVD, PROMO REELS AND VIDEOS ON TIME AND ON BUDGET."

I need to create a flyer/ad that I will use to promote myself and the services I provide.

My name is Bertrand Kowalczyk and I am a music video clip director and editor that can achieve great results regardless of budgets.

Working with HD and Super 8 vintage film formats to achieve the look you want.

I am a Melbourne based film maker with a huge client list; 518, Mardewick, Queen Lanterns, June Farrow, Dora-Mae, Brackenmoor, The Plovers, Lionel Brabham, Pinecone Marketing, OVX and Dunmore City Council.

Black and white classic design. Clean and neat not too busy, almost minimal in a way. Incorpirate my initials to create a logo perhaps.

It needs to appeal and relate to various music genres including; rock, pop, soul, funk, country and folk as I make music videos for artists of many genres.

Feature my website:

www.clipvault-example.net/berkowal

Include my email address

bertrandkowalczyk@mailnest-example.net

Many thanks

Bertrand

Target Market(s)

Music artists and bands performing all sorts of music styles from; rock, soul, funk, pop, country and folk.

Appealing also to band managers, artist representation and record labels/music publishers.

Industry/Entity Type

Artists

Requirements
Must have
• My website and email address and my name. I am a sole trader so i don't have a business name as such, just my name, Bertrand Kowalczyk.
Should not have
• a picture of me

```html
<!DOCTYPE html>
<html lang="en">
<head>
<meta charset="utf-8">
<title>Bertrand Kowalczyk – Film and Music Video Director</title>
<link rel="stylesheet" href="https://fonts.googleapis.com/css2?family=Source+Sans+3:wght@300;400;700;900&display=swap">
<style>
  :root {
    --paper: #ffffff;
    --brand-blue: #1a73b8;
    --panel-grey: #e6e7e8;
    --edge-grey: #77787b;
    --art-dark: #9c9da0;
    --art-mid: #bfc0c2;
    --art-soft: #dcdddf;
    --ink-strong: #111111;
    --ink-body: #3a3a3c;
  }
  * { margin: 0; padding: 0; box-sizing: border-box; }
  html, body {
    width: 1200px;
    height: 2700px;
    overflow: hidden;
    background: var(--paper);
  }
  .flyer {
    position: relative;
    width: 1200px;
    height: 2700px;
    background: var(--paper);
    font-family: "Source Sans 3", sans-serif;
    overflow: hidden;
  }
  .hero-art {
    position: absolute;
    left: 60px;
    top: 210px;
    width: 1140px;
    height: 1000px;
    background:
      radial-gradient(ellipse 24% 46% at 72% 38%, var(--art-dark) 0%, var(--art-mid) 45%, rgba(255,255,255,0) 100%),
      radial-gradient(ellipse 26% 30% at 24% 66%, var(--art-mid) 0%, var(--art-soft) 50%, rgba(255,255,255,0) 100%),
      radial-gradient(ellipse 55% 50% at 50% 55%, var(--art-soft) 0%, rgba(255,255,255,0) 100%);
  }
  .name-bar {
    position: absolute;
    left: 84px;
    top: 90px;
    width: 1068px;
    height: 225px;
    background: var(--brand-blue);
    display: flex;
    align-items: center;
    justify-content: center;
  }
  .name-bar h1 {
    color: var(--paper);
    font-weight: 300;
    font-size: 124px;
    white-space: nowrap;
    line-height: 1;
  }
  .panel-shapes {
    position: absolute;
    left: 0;
    top: 0;
    width: 1200px;
    height: 2700px;
  }
  .panel-shapes .info-panel { fill: var(--panel-grey); }
  .panel-shapes .panel-edge { fill: var(--edge-grey); }
  .service-copy {
    position: absolute;
    left: 282px;
    top: 1232px;
    width: 900px;
    color: var(--ink-body);
  }
  .service-copy .kicker {
    font-weight: 900;
    font-size: 44px;
    color: var(--ink-strong);
    line-height: 1;
  }
  .service-copy .role {
    font-weight: 900;
    font-size: 116px;
    color: var(--ink-strong);
    line-height: 93px;
    letter-spacing: -1px;
    margin-top: 2px;
    white-space: nowrap;
  }
  .service-copy .details {
    font-weight: 300;
    font-size: 44px;
    line-height: 60px;
    margin-top: 8px;
    white-space: nowrap;
  }
  .service-copy .details strong,
  .service-copy .formats strong {
    font-weight: 700;
    color: var(--ink-strong);
  }
  .service-copy .formats {
    font-weight: 300;
    font-size: 61px;
    line-height: 75px;
    margin-top: 10px;
    white-space: nowrap;
  }
  .contact {
    position: absolute;
    left: 0;
    top: 2455px;
    width: 1200px;
    text-align: center;
    font-weight: 400;
    font-size: 40px;
    line-height: 62px;
    color: var(--ink-body);
  }
</style>
</head>
<body>
  <main class="flyer">
    <div class="hero-art" role="img" aria-label="Grey illustration of a vintage studio microphone and a film reel"></div>

    <svg class="panel-shapes" viewBox="0 0 1200 2700" aria-hidden="true">
      <polygon class="info-panel" points="246,1161 1200,1116 1200,2310 246,2346"/>
      <polygon class="panel-edge" points="84,1152 246,1104 246,2190 204,2190"/>
    </svg>

    <header class="name-bar">
      <h1>Bertrand Kowalczyk</h1>
    </header>

    <section class="service-copy">
      <p class="kicker">PROFESSIONAL</p>
      <h2 class="role">FILM AND MUSIC<br>VIDEO DIRECTOR</h2>
      <p class="details">
        WITH OVER <strong>10 YEARS EXPERIENCE</strong>.<br>
        CLIENT LIST INCLUDES, 518, MARDEWICK,<br>
        QUEEN LANTERNS, BRACKENMOOR, THE<br>
        PLOVERS, TAN FOG, DORA-MAE, JUNE FARROW,<br>
        OVX, PINECONE.
      </p>
      <p class="formats">
        HD, SUPER 8, LIVE DVD, PROMO<br>
        REELS AND VIDEOS <strong>ON TIME</strong><br>
        AND <strong>ON BUDGET</strong>
      </p>
    </section>

    <footer class="contact">
      <p>www.clipvault-example.net/berkowal</p>
      <p>bertrandkowalczyk@mailnest-example.net</p>
    </footer>
  </main>
</body>
</html>
```